Buch-/eBook-Cover Budgetplanung
Zielgruppe
Ich bin Autorin und verkaufe unter meiner Marke SparLaterne Bücher und handgemachte Produkte rund um Budgetplanung und bewussten Umgang mit Geld. Meine Zielgruppe sind Frauen ab 45, die ihre Finanzen ordnen und bewusster leben möchten. Sie mögen eine ruhige, hochwertige, leicht nostalgische Ästhetik und werden von lauten, grellen Designs abgeschreckt.
Aufgabenstellung
Buchcover 'Der leere Korb' (VRL), Auftakt einer Cover-Serie
Das Buch:
Ratgeber über bewussten Konsumverzicht: ein Jahr Kaufpause mit monatlichen Challenges. Warm und ermutigend, kein Verbotsbuch. Zielgruppe: Frauen ab 45, die eine ruhige, hochwertige, leicht nostalgische Ästhetik mögen.
Texte auf dem Cover:
Titel: Der leere Korb
Untertitel: Die No-Buy-Challenge: Ein Jahr bewusst nicht kaufen, Geld sparen und herausfinden, was du wirklich brauchst
Autorin: Helene Morwitz
Serie:
Weitere Geld-Ratgeber von mir erhalten danach Cover im selben Stil. Gesucht ist also ein wiederholbares Layout, bei dem sich pro Buch nur Titel und Motiv ändern. Der Gewinner erhält die Folgecover als Direktaufträge.
Stil (Referenzbilder anbei, bitte verbindlich umsetzen):
Marke SparLaterne: Graublau (#95a9af) und Creme, Gold nur als Akzent. Vertikale Streifen als Markenmuster, weiße Spitzenborte, schwarze handgezeichnete Schleife (PNG liegt bei). Schriften: Cormorant Garamond für Versalien, Sloop Pro, Kalligrafieschrift für Akzente. Wirkung: elegantes, feminines Vintage. Das Buchinnere ist bereits in diesem Stil gestaltet (Beispielseiten anbei), das Cover soll dazu passen.
Bitte nicht: Geldscheine, Münzen, Sparschweine, Einkaufstüten, rote Verbotssymbole, grelle Farben, Rosa, überfüllte Layouts.
Wichtigstes Kriterium:
Der Titel muss als kleines Lunova-Vorschaubild klar lesbar sein.
Lieferumfang:
E-Book-Cover (JPG, 2560 x 1600 px), VRL-Print-Umschlag (6 x 9 Zoll, 159 Seiten, Farbdruck)
Das Design darf nicht zu überladen sein.

```html
<!DOCTYPE html>
<html lang="de">
<head>
<meta charset="utf-8">
<title>Der leere Korb – Helene Morwitz</title>
<link rel="stylesheet" href="https://fonts.googleapis.com/css2?family=Bebas+Neue&family=Carlito&display=swap">
<style>
  :root {
    --cream: #f6f2ec;
    --stripe-blue: #c5cfd1;
    --ornament-blue: #b7c6cb;
    --gold: #d3aa6a;
    --ink: #2f2f2f;
    --bow-grey: #a3a3a3;
  }
  html, body {
    margin: 0;
    padding: 0;
    overflow: hidden;
    background: var(--cream);
  }
  .cover {
    position: relative;
    width: 929px;
    height: 1200px;
    overflow: hidden;
    background: repeating-linear-gradient(
      90deg,
      var(--cream) 0 49px,
      var(--stripe-blue) 49px 85px
    );
    background-position: 18px 0;
  }
  .ornament-border {
    position: absolute;
    inset: 0;
    width: 929px;
    height: 1200px;
  }
  .bow-motif {
    position: absolute;
    left: 212px;
    top: 243px;
    width: 204px;
    height: 250px;
    border-radius: 40px;
    background: var(--bow-grey);
    opacity: 0.35;
  }
  .title {
    position: absolute;
    left: 0;
    right: 0;
    top: 226px;
    margin: 0;
    text-align: center;
    font-family: "Bebas Neue", sans-serif;
    font-weight: 400;
    font-size: 162px;
    line-height: 129px;
    color: var(--gold);
    text-shadow: 6px 6px 0 var(--ink);
  }
  .title span { display: block; }
  .subtitle-head {
    position: absolute;
    left: 0;
    right: 0;
    top: 628px;
    margin: 0;
    text-align: center;
    font-family: "Bebas Neue", sans-serif;
    font-weight: 400;
    font-size: 48px;
    line-height: 48px;
    color: var(--ink);
  }
  .subtitle {
    position: absolute;
    left: 0;
    right: 0;
    top: 690px;
    margin: 0;
    text-align: center;
    font-family: "Carlito", sans-serif;
    font-size: 24px;
    line-height: 34px;
    color: var(--ink);
  }
  .author {
    position: absolute;
    left: 0;
    right: 0;
    top: 955px;
    margin: 0;
    text-align: center;
    font-family: "Bebas Neue", sans-serif;
    font-weight: 400;
    font-size: 45px;
    line-height: 45px;
    color: var(--ink);
  }
</style>
</head>
<body>
  <main class="cover">
    <svg class="ornament-border" viewBox="0 0 929 1200" role="img" aria-label="Bordüre aus graublauen Spiralornamenten rund um den Umschlag">
      <path fill="var(--ornament-blue)" fill-rule="evenodd"
        d="M0 0H929V1200H0Z M52 56V1144H877V56Z"/>
    </svg>

    <div class="bow-motif" role="img" aria-label="Handgezeichnete graue Schleife am Titel"></div>

    <h1 class="title">
      <span>Der</span>
      <span>leere</span>
      <span>Korb</span>
    </h1>

    <p class="subtitle-head">Die No-Buy-Challenge:</p>

    <p class="subtitle">
      Ein Jahr bewusst nicht kaufen,<br>
      Geld sparen und herausfinden,<br>
      was du wirklich brauchst
    </p>

    <p class="author">Helene Morwitz</p>
  </main>
</body>
</html>
```